Centro Veterinário Solarena
Já é o terceiro serviço que contrato na plataforma e sempre sou bem atendida e fico muito satisfeita com os resultados!
Heitor, fiquei muito satisfeita com o seu suporte! Nos ajudou demais no alinhamento! Muitíssimo obrigada!

```html
<!DOCTYPE html>
<html lang="pt-BR">
<head>
<meta charset="UTF-8">
<title>Centro Veterinário Solarena — Pasta</title>
<link rel="stylesheet" href="https://fonts.googleapis.com/css2?family=Marcellus&family=Montserrat:wght@400;500&display=swap">
<style>
  :root {
    --paper: #ffffff;
    --navy: #262c37;
    --navy-line: #353c4a;
    --copper: #c39a79;
    --ink: #2b303a;
    --muted: #c7cad0;
  }
  * { margin: 0; padding: 0; box-sizing: border-box; }
  html, body { width: 1200px; height: 1200px; overflow: hidden; background: var(--paper); }
  .folder { position: relative; width: 1200px; height: 1200px; }
  .folder-shapes { position: absolute; inset: 0; }

  .brand {
    position: absolute; left: 760px; top: 270px; width: 400px;
    text-align: center; color: var(--ink);
    font-family: "Marcellus", serif; font-weight: 400;
  }
  .brand-mark {
    width: 110px; height: 110px; margin: 0 auto 26px;
    border: 2px solid var(--ink); border-radius: 50%;
  }
  .brand-line-small { font-size: 25px; letter-spacing: 1px; }
  .brand-line-large { font-size: 58px; line-height: 1.05; }

  .contact {
    position: absolute; left: 260px; top: 790px; width: 200px;
    font-family: "Montserrat", sans-serif; color: var(--muted);
    font-size: 9.5px; line-height: 1.35;
  }
  .contact-mark {
    width: 80px; height: 80px; margin: 0 0 12px 10px;
    border: 1.5px solid var(--muted); border-radius: 50%;
  }
  .contact-address { margin-bottom: 10px; padding-left: 22px; }
  .contact-list { list-style: none; }
  .contact-item { display: flex; align-items: center; gap: 6px; margin-bottom: 6px; }
  .contact-icon { width: 14px; height: 14px; flex: none; }
</style>
</head>
<body>
<main class="folder">
  <svg class="folder-shapes" width="1200" height="1200" viewBox="0 0 1200 1200" aria-hidden="true">
    <path class="back-panel" d="M0 815 Q600 500 1200 815 L1200 1128 L0 1128 Z" fill="var(--navy)"/>
    <path class="panel-line" d="M230 1128 Q480 760 1200 700" fill="none" stroke="var(--navy-line)" stroke-width="6"/>
    <path class="accent-arc" d="M650 594 Q1020 600 1200 730" fill="none" stroke="var(--copper)" stroke-width="3"/>
    <rect class="card-slot-frame" x="758" y="842" width="188" height="106" rx="18" fill="none" stroke="#59606c" stroke-width="2"/>
    <rect class="card-slot" x="766" y="850" width="172" height="90" rx="13" fill="var(--paper)"/>
  </svg>

  <header class="brand">
    <div class="brand-mark"></div>
    <div class="brand-line-small">Centro Veterinário</div>
    <div class="brand-line-large">Solarena</div>
  </header>

  <section class="contact">
    <div class="contact-mark"></div>
    <p class="contact-address">Rua das Acácias, 312<br>Jardim Paraíso<br>Vila Serena - BA</p>
    <ul class="contact-list">
      <li class="contact-item">
        <svg class="contact-icon" viewBox="0 0 16 16"><circle cx="8" cy="8" r="7" fill="none" stroke="var(--copper)" stroke-width="1.2"/><path d="M5.5 4.5 L7 6 L6.2 7.2 Q7.3 9 8.8 9.8 L10 9 L11.5 10.5 L10.6 11.6 Q6 11 4.4 5.4 Z" fill="var(--copper)"/></svg>
        <span>77 98000-4521</span>
      </li>
      <li class="contact-item">
        <svg class="contact-icon" viewBox="0 0 16 16"><rect x="2" y="4" width="12" height="8" rx="1" fill="none" stroke="var(--copper)" stroke-width="1.2"/><path d="M2.5 4.5 L8 9 L13.5 4.5" fill="none" stroke="var(--copper)" stroke-width="1.2"/></svg>
        <span>contato@solarena.vet</span>
      </li>
      <li class="contact-item">
        <svg class="contact-icon" viewBox="0 0 16 16"><circle cx="8" cy="8" r="6" fill="none" stroke="var(--copper)" stroke-width="1.2"/></svg>
        <span>@solarena.vet</span>
      </li>
      <li class="contact-item">
        <svg class="contact-icon" viewBox="0 0 16 16"><circle cx="8" cy="8" r="6" fill="none" stroke="var(--copper)" stroke-width="1.2"/><ellipse cx="8" cy="8" rx="2.6" ry="6" fill="none" stroke="var(--copper)" stroke-width="1"/><path d="M2 8 H14" stroke="var(--copper)" stroke-width="1"/></svg>
        <span>www.solarena.vet.br</span>
      </li>
    </ul>
  </section>
</main>
</body>
</html>
```